Renewed electronic office supplies

I need a landing page design for a B2B business that will sell refurbished and renewed electronic devices such as smartphones, laptops, tablets and other gadgets. We want to become suppliers of these devices to companies that need computers and other devices for their employees. The point of our business is that they can get a great device that is in very good contrition instead of buying brand new. Companies will be able to save 50-60% on these renewed devices. Not only that we will also buy the companies old devices which they no longe needs and renew them and give them new life so we can resell it.

Our services will be:

- sale of renewed devices with lifetime warranty

- purchase of old devices

- swap solution: meaning client buy from us and sell at the same time so we deduct the amount sale of their old devices into their purchase.

Some useful information:

- company name and logo are still pending

- we aim to provide all business with top quality of renewed and environmentally friendly electronics, while maintaining a minimal impact on the natural environment.

I have attached a word document with some additional info that might be useful

Looking forward to seeing all your great designs!

P.s. Please feel free to make designs that are not based on my documents also, we need different layouts and designs. as for now I see many of the designs are more or less the same. we need more variation on design
Updates

Target Market(s)

Medium to large Businesses

Industry/Entity Type

Technology Equipment

Requirements
Must have
• we need more designs to be submitted , 50 designs minimum

```html
<!DOCTYPE html>
<html lang="en">
<head>
<meta charset="utf-8">
<title>Reusable Electronic Office Supplies</title>
<link rel="stylesheet" href="https://fonts.googleapis.com/css2?family=Poppins:wght@300;400;500;600;700&family=Alfa+Slab+One&display=swap">
<style>
:root{
  --red:#d8190e;
  --black:#000000;
  --ink:#111111;
  --grey:#666666;
  --soft:#f6f6f6;
  --line:#e2e2e2;
  --white:#ffffff;
  --night:#0d0f1a;
}
*{margin:0;padding:0;box-sizing:border-box}
html,body{width:1200px;height:3480px;overflow:hidden;background:var(--white)}
body{position:relative;font-family:"Poppins",sans-serif;color:var(--ink)}
.abs{position:absolute}

/* header */
.brand{left:61px;top:18px;font-size:30px;font-weight:600;color:var(--ink);letter-spacing:-0.3px}
.call{left:982px;top:24px;display:flex;gap:10px;align-items:center}
.call small{display:block;font-size:11px;color:var(--red);font-weight:500}
.call b{display:block;font-size:16px;font-weight:500;color:var(--ink);letter-spacing:.5px}

/* hero */
.hero-bg{left:0;top:82px;width:1200px;height:640px}
.hero-title{left:61px;top:198px;font-family:"Alfa Slab One",serif;font-size:45px;line-height:57px;color:var(--white);letter-spacing:.5px}
.hero-title .accent{color:var(--red)}
.hero-text{left:61px;top:378px;width:420px;font-size:14px;line-height:24px;color:#e4e4e4;font-weight:300}
.btn{display:inline-flex;align-items:center;justify-content:center;font-size:13px;font-weight:500;text-transform:uppercase}
.btn-red{background:var(--red);color:var(--white)}
.btn-ghost{border:1.5px solid var(--white);color:var(--white)}
.hero-shop{left:61px;top:473px;width:119px;height:43px}
.hero-more{left:195px;top:473px;width:120px;height:43px}
.hero-phone{left:648px;top:186px;width:416px;height:525px;border-radius:34px;background:linear-gradient(110deg,#3c4247 0%,#707a82 35%,#1a1c22 50%,#6f8fd6 65%,#c6d6f5 85%,#3556b8 100%)}

/* section headings */
.sec-title{left:0;width:1200px;text-align:center;font-size:33px;font-weight:500;color:var(--ink)}
.sec-mark{left:520px;width:160px;height:8px}
.sec-mark::before{content:"";position:absolute;left:0;right:0;top:3px;height:1px;background:var(--line)}
.sec-mark::after{content:"";position:absolute;left:76px;top:0;width:8px;height:8px;border-radius:50%;background:var(--red)}

/* feature rows */
.dots{width:150px;height:150px;background:#f1f1f1}
.bar{width:38px;height:149px;background:var(--red)}
.photo{width:361px;height:239px}
.feat-head{font-size:24px;font-weight:500;color:var(--red);line-height:31px}
.feat-text{font-size:11px;line-height:19px;color:var(--grey);font-weight:300}
.feat-text p+p{margin-top:11px}

/* products */
.card{top:1987px;width:225px;height:300px;background:var(--soft)}
.card-img{top:1925px;height:142px}
.card-name{top:2112px;width:225px;text-align:center;font-size:18px;font-weight:500}
.card-text{top:2151px;width:225px;padding:0 18px;text-align:center;font-size:11px;line-height:19px;color:var(--grey);font-weight:300}
.card-btn{top:2222px;width:90px;height:29px;font-size:10px}

/* help panels */
.panel{top:2460px;width:360px;height:240px;color:var(--white);text-align:center}
.panel-red{left:240px;background:var(--red)}
.panel-black{left:600px;background:var(--black)}
.panel svg{position:absolute;left:150px;top:36px}
.panel h3{position:absolute;left:0;right:0;top:116px;font-size:21px;font-weight:500}
.panel p{position:absolute;left:40px;right:40px;top:162px;font-size:12px;line-height:21px;font-weight:300}

/* cta */
.cta-band{left:0;top:2850px;width:1200px;height:256px}
.cta-devices{left:426px;top:2774px;width:331px;height:185px;border-radius:6px;background:linear-gradient(120deg,#e9eef5 0%,#7fa8d8 40%,#5a2a7a 65%,#c05a9c 85%,#2b2b3a 100%)}
.cta-small{left:327px;top:2994px;font-size:11px;color:var(--white);font-weight:300}
.cta-big{left:327px;top:3015px;font-size:27px;color:var(--white);font-weight:400}
.cta-btn{left:736px;top:2997px;width:135px;height:51px;background:var(--white);color:var(--ink);font-size:13px}

/* footer */
.footer{left:0;top:3105px;width:1200px;height:375px;background:var(--black)}
.foot-brand{left:61px;top:3175px;font-size:24px;font-weight:600;color:var(--red)}
.foot-head{top:3178px;font-size:18px;font-weight:500;color:var(--red)}
.foot-about{left:61px;top:3221px;width:240px;font-size:11px;line-height:22px;color:var(--white);font-weight:300}
.foot-list{top:3220px;list-style:none;font-size:12px;color:var(--white);font-weight:300}
.foot-list li{height:24px;line-height:24px}
.foot-list li::before{content:"-";margin-right:10px}
.social{top:3225px;width:34px;height:34px}
.foot-rule{left:61px;top:3413px;width:1080px;height:1px;background:#2a2a2a}
.copyright{left:0;top:3440px;width:1200px;text-align:center;font-size:11px;color:#9a9a9a;font-weight:300}
</style>
</head>
<body>

<header>
  <div class="abs brand">Company Name</div>
  <div class="abs call">
    <svg width="32" height="32" viewBox="0 0 32 32" aria-hidden="true">
      <path d="M8 5l4 0 2 6-3 2c1.5 3.5 4.5 6.5 8 8l2-3 6 2 0 4c0 1.5-1.5 3-3 3C13 27 5 19 5 8c0-1.5 1.5-3 3-3z" fill="none" stroke="#d8190e" stroke-width="2.2" stroke-linejoin="round"/>
      <path d="M18 6a8 8 0 0 1 8 8M18 2a12 12 0 0 1 12 12" fill="none" stroke="#d8190e" stroke-width="2" stroke-linecap="round"/>
    </svg>
    <div><small>Call Us Now</small><b>123.456.7890</b></div>
  </div>
</header>

<section class="hero">
  <svg class="abs hero-bg" viewBox="0 0 1200 640" role="img" aria-label="Dark city night photograph with blurred lights">
    <defs>
      <linearGradient id="heroShade" x1="0" y1="0" x2="1" y2="1">
        <stop offset="0" stop-color="#151722"/>
        <stop offset="0.45" stop-color="#2a2226"/>
        <stop offset="1" stop-color="#0b0d18"/>
      </linearGradient>
    </defs>
    <polygon points="0,0 1200,0 1200,573 601,638 0,558" fill="url(#heroShade)"/>
    <polygon points="0,558 601,638 0,598" fill="#d8190e"/>
  </svg>
  <h1 class="abs hero-title">REUSABLE<br>ELECTRONIC<br><span class="accent">OFFICE SUPPLIES</span></h1>
  <p class="abs hero-text">we aim to provide all business with top quality of reused and environmentally friendly electronics, while maintaining a minimal impact on the natural environment.</p>
  <a class="abs btn btn-red hero-shop">Shop Now</a>
  <a class="abs btn btn-ghost hero-more">Check More</a>
  <div class="abs hero-phone" role="img" aria-label="Smartphone shown from back and front"></div>
</section>

<section class="why">
  <h2 class="abs sec-title" style="top:788px">Why Choose Us</h2>
  <div class="abs sec-mark" style="top:841px"></div>

  <div class="abs dots" style="left:135px;top:1027px" role="img" aria-label="Dot grid decoration"></div>
  <div class="abs bar" style="left:188px;top:938px"></div>
  <div class="abs photo" style="left:224px;top:892px;background:linear-gradient(120deg,#fbf3e6,#e3b98a 55%,#b98a5e)" role="img" aria-label="Laptop with cardboard boxes"></div>
  <div class="abs" style="left:646px;top:913px;width:380px">
    <h3 class="feat-head">A smarter circular solution for electronic supplies</h3>
    <div class="feat-text" style="margin-top:18px">
      <p>Billions of electronics are being made, sold, and disposed of every year – a cycle that drives short-term profits for electronics manufacturers, but at too high a cost for the planet we all share.</p>
      <p>With our experience in the recycling market we can put an end to this cycle and offer a circular solution that is both affordable and environmentally friendly.</p>
    </div>
  </div>

  <div class="abs dots" style="left:906px;top:1333px" role="img" aria-label="Dot grid decoration"></div>
  <div class="abs bar" style="left:974px;top:1252px"></div>
  <div class="abs photo" style="left:615px;top:1208px;background:linear-gradient(110deg,#3a3632,#8d7a6a 45%,#d9d4cf)" role="img" aria-label="Hand holding a smartphone"></div>
  <div class="abs" style="left:189px;top:1278px;width:360px">
    <h3 class="feat-head">Buy reusable IT</h3>
    <div class="feat-text" style="margin-top:12px">
      <p>We specialize in refurbished electronic devices with top quality for affordable prices. All our products have undergone a detailed testing and reconditioning program by expert technicians.</p>
    </div>
  </div>

  <div class="abs dots" style="left:135px;top:1483px" role="img" aria-label="Dot grid decoration"></div>
  <div class="abs bar" style="left:188px;top:1567px"></div>
  <div class="abs photo" style="left:224px;top:1523px;background:linear-gradient(120deg,#2e2b2b,#5a524a 50%,#a59c90)" role="img" aria-label="Hands using a smartphone at a table"></div>
  <div class="abs" style="left:646px;top:1593px;width:370px">
    <h3 class="feat-head">Sell your IT Safely</h3>
    <div class="feat-text" style="margin-top:12px">
      <p>We can also buy your used electronics and make sure they get reused and give them a new life. By selling your used devices that you no longer have use for you can help us create carbon savings.</p>
    </div>
  </div>
</section>

<section class="products">
  <h2 class="abs sec-title" style="top:1830px">Our Products</h2>
  <div class="abs sec-mark" style="top:1882px"></div>

  <div class="abs card" style="left:116px"></div>
  <div class="abs card-img" style="left:190px;width:78px;border-radius:6px;background:linear-gradient(160deg,#2a2a2a,#3a5ea8 60%,#111)" role="img" aria-label="Smartphone"></div>
  <div class="abs card-name" style="left:116px">Smartphones</div>
  <p class="abs card-text" style="left:116px">Lorem ipsum dolor consectetur adipiscing elit, sed eiusmod dolore magna aliqua.</p>
  <a class="abs btn btn-red card-btn" style="left:184px">Shop Now</a>

  <div class="card abs" style="left:363px"></div>
  <div class="abs card-img" style="left:383px;width:186px;background:linear-gradient(120deg,#6aa23a,#2c2c2c 45%,#9a9a9a 75%,#1a1a1a)" role="img" aria-label="Assorted gadgets and devices"></div>
  <div class="abs card-name" style="left:363px">Gadgets</div>
  <p class="abs card-text" style="left:363px">Lorem ipsum dolor consectetur adipiscing elit, sed eiusmod dolore magna aliqua.</p>
  <a class="abs btn btn-red card-btn" style="left:431px">Shop Now</a>

  <div class="card abs" style="left:611px"></div>
  <div class="abs card-img" style="left:636px;width:176px;height:136px;background:linear-gradient(160deg,#1d2230,#8a2020 50%,#1a1a1a)" role="img" aria-label="Laptop"></div>
  <div class="abs card-name" style="left:611px">Laptops</div>
  <p class="abs card-text" style="left:611px">Lorem ipsum dolor consectetur adipiscing elit, sed eiusmod dolore magna aliqua.</p>
  <a class="abs btn btn-red card-btn" style="left:678px">Shop Now</a>

  <div class="card abs" style="left:858px"></div>
  <div class="abs card-img" style="left:926px;width:90px;height:137px;border-radius:6px;background:linear-gradient(160deg,#1a1a1a,#7b9cc9 50%,#1a1a1a)" role="img" aria-label="Tablet"></div>
  <div class="abs card-name" style="left:858px">Tablets</div>
  <p class="abs card-text" style="left:858px">Lorem ipsum dolor consectetur adipiscing elit, sed eiusmod dolore magna aliqua.</p>
  <a class="abs btn btn-red card-btn" style="left:925px">Shop Now</a>
</section>

<section class="help">
  <h2 class="abs sec-title" style="top:2355px">We're Glad To help</h2>
  <div class="abs sec-mark" style="top:2407px"></div>

  <div class="abs panel panel-red">
    <svg width="60" height="60" viewBox="0 0 60 60" aria-hidden="true" fill="none" stroke="#fff" stroke-width="2.2" stroke-linejoin="round" stroke-linecap="round">
      <path d="M4 6h9l7 30h28l6-22H16"/>
      <path d="M18 21h34M19 28h31M26 14l2 22M35 14l1 22M44 14l-1 22"/>
      <path d="M20 36l-3 8h33"/>
      <circle cx="22" cy="51" r="4"/><circle cx="44" cy="51" r="4"/>
    </svg>
    <h3>Buy From Us</h3>
    <p>Lorem ipsum dolor sit amet, consectetur adip labore et dolore magna aliqua.</p>
  </div>
  <div class="abs panel panel-black">
    <svg width="60" height="60" viewBox="0 0 60 60" aria-hidden="true" fill="none" stroke="#fff" stroke-width="2" stroke-linejoin="round" stroke-linecap="round">
      <circle cx="30" cy="18" r="12"/>
      <path d="M33 13c-1-2-6-2-6 1s6 2 6 5-5 3-6 1M30 9v3M30 24v3"/>
      <path d="M6 38h10l8 4h10c2 0 2 4 0 4H24M16 52l8 4h14l14-10c2-2 0-5-2-4l-12 6"/>
      <rect x="2" y="36" width="6" height="18"/>
      <rect x="44" y="44" width="10" height="10"/>
    </svg>
    <h3>Sell To Us</h3>
    <p>Lorem ipsum dolor sit amet, consectetur adip labore et dolore magna aliqua.</p>
  </div>
</section>

<section class="cta">
  <svg class="abs cta-band" viewBox="0 0 1200 256" preserveAspectRatio="none" aria-hidden="true">
    <polygon points="0,68 470,0 730,0 1200,68 1200,256 0,256" fill="#d8190e"/>
  </svg>
  <div class="abs cta-devices" role="img" aria-label="Group of smartphones, tablet and laptop"></div>
  <p class="abs cta-small">Lorem ipsum dolor sit amet, consectetur adipiscing elit.</p>
  <p class="abs cta-big">Register your interest with us.</p>
  <a class="abs btn cta-btn">Sign In Now</a>
</section>

<footer>
  <div class="abs footer"></div>
  <div class="abs foot-brand">Company Name</div>
  <p class="abs foot-about">Lorem ipsum dolor sit amet, consectetur adipiscing elit, sed do eiusmod tempor incididunt &nbsp;magna aliqua.</p>

  <div class="abs foot-head" style="left:336px">Help</div>
  <ul class="abs foot-list" style="left:336px">
    <li>Home</li><li>About</li><li>Sell</li><li>Buy</li><li>Contact</li>
  </ul>

  <div class="abs foot-head" style="left:613px">Products</div>
  <ul class="abs foot-list" style="left:613px">
    <li>Smartphones</li><li>Laptops</li><li>Tablets</li><li>Gadgets</li>
  </ul>

  <div class="abs foot-head" style="left:888px">Social Media</div>
  <span class="abs social" style="left:888px;background:#4a67ad" aria-label="Social link"></span>
  <span class="abs social" style="left:932px;background:#2aa3ef" aria-label="Social link"></span>
  <span class="abs social" style="left:977px;background:#1f7bb6" aria-label="Social link"></span>
  <span class="abs social" style="left:1021px;background:#e0487a" aria-label="Social link"></span>

  <div class="abs foot-rule"></div>
  <p class="abs copyright">Copyright © COMPANY NAME – 2020. All Right Reserved.</p>
</footer>

</body>
</html>
```